Business Card (double-sided) and Stationary Design for dental office

1) Business Card Design: We need a business card design for a dental specialty office.
Texts should contain:
The name of our office "Bayhaven Grins Orthodontics"
Tagline: "Specialist in Orthodontic and Maxillofacial Orthopedics"
Tag line: "Creating "Talvering" smiles for Children and Adults"
Doctor name: "Doctor Name"
Office Address:
"123 Street Name
City, State Zip code"
Office email address: office@bayhavengrins.com
Website: www.bayhavengrins.com

We will provide the full office address once the design is selected
Theme: beach, paradise, coastal, wave
We would like to have some creativity in design. Some acceptable ideas: front page: logo and office name. Back page: more detail information, and map to office in form of an island. Please see sample from our other location, but you DON'T HAVE TO USE OR COPY THE SAME CONCEPT.

IF POSSIBLE, PLEASE SUBMIT AT LEAST TWO CONCEPTS: ONE WITH THE BACK LOOKING SIMILAR TO WHAT IS IN THE SAMPLE, AND ONE DIFFERENT.

Color: designer to choose. We have different shade of blues and sand color in our office. Please see logo.

2) Please also design a matching set of stationary that compliment the business card and our logo.

Target Market(s)

Dental

Contact Information for Business Card

See descriptions

Font styles to use
Other font styles liked:
• Matching texts in logo

Colors
0054AA
0677BA
7BADD7
CADEEF
E8F1F8
0094D4
00A9DD
6FCCEA
C7EBF8
E9F6FB
00AB8E
00BBA5
67D7C9
C6EFE9
E9F9F6

Requirements
Must have
• Double-sided
Nice to have
• Beach coastal theme
Should not have
• Any shape or drawing of of tooth or teeth. We don’t need these. You don't necessarily have to just cut and paste the logo art and text as a whole, you have the liberty to rearrange the text.

```html
<!DOCTYPE html>
<html lang="en">
<head>
<meta charset="utf-8">
<title>Bayhaven Grins – Business Card</title>
<link rel="stylesheet" href="https://fonts.googleapis.com/css2?family=Open+Sans:wght@600;700&family=Arimo:wght@400&display=swap">
<style>
  :root {
    --page: #e6e6e4;
    --paper: #f7f7f6;
    --ocean: #2f7f9c;
    --ocean-deep: #276c86;
    --seafoam: #76c6b6;
    --ink: #4a4a4a;
    --charcoal: #2a2b2e;
    --charcoal-edge: #1f2023;
    --emboss: #1b1c1e;
    --white: #ffffff;
  }
  * { box-sizing: border-box; margin: 0; padding: 0; }
  html, body { width: 1200px; height: 801px; overflow: hidden; }
  body {
    background: var(--page);
    position: relative;
    font-family: "Arimo", Arial, sans-serif;
  }
  .card {
    position: absolute;
    top: 246px;
    width: 540px;
    height: 309px;
    overflow: hidden;
    box-shadow: 0 6px 18px rgba(0,0,0,0.18);
  }
  .card--front { left: 40px; background: var(--paper); border-bottom: 3px solid var(--seafoam); }
  .card--back {
    left: 620px;
    background: linear-gradient(135deg, var(--charcoal-edge), var(--charcoal));
    border-bottom: 3px solid var(--seafoam);
  }

  .wave { position: absolute; inset: 0; }

  .name-tab {
    position: absolute; top: 0; right: 46px;
    width: 14px; height: 26px;
    background: var(--seafoam);
    border-radius: 0 0 3px 3px;
  }
  .person {
    position: absolute; top: 20px; right: 70px;
    text-align: right;
  }
  .person__name {
    font-family: "Open Sans", sans-serif;
    font-weight: 700; font-size: 18px; line-height: 1.2;
    color: var(--seafoam);
  }
  .person__role { font-size: 12px; color: var(--ink); margin-top: 2px; }

  .brand {
    position: absolute; left: 30px; top: 112px;
    display: flex; align-items: center; gap: 12px;
  }
  .brand__dot {
    width: 50px; height: 50px; border-radius: 50%;
    background: var(--ocean); flex: none;
  }
  .brand__name {
    font-family: "Open Sans", sans-serif;
    font-weight: 700; font-size: 26px;
    color: var(--ocean); line-height: 1;
  }
  .brand__tagline {
    font-family: "Open Sans", sans-serif;
    font-weight: 600; font-size: 10px;
    letter-spacing: 0.5px;
    color: var(--seafoam); margin-top: 6px;
    border-top: 1.5px solid var(--ocean);
    padding-top: 3px;
  }

  .address {
    position: absolute; left: 92px; top: 198px;
    font-size: 13px; line-height: 1.4; color: var(--ink);
  }

  .contact {
    position: absolute; right: 16px; top: 135px;
    list-style: none; text-align: right;
    color: var(--white); font-size: 11.5px; line-height: 20px;
  }
  .contact li { display: flex; align-items: center; justify-content: flex-end; gap: 7px; }
  .contact svg { width: 12px; height: 12px; flex: none; }

  .back-brand {
    position: absolute; left: 0; right: 0; top: 92px;
    display: flex; flex-direction: column; align-items: center;
  }
  .back-brand__dot {
    width: 70px; height: 70px; border-radius: 50%;
    background: var(--emboss);
    box-shadow: inset 1px 1px 2px rgba(255,255,255,0.12), inset -1px -1px 3px rgba(0,0,0,0.5);
  }
  .back-brand__name {
    font-family: "Open Sans", sans-serif;
    font-weight: 700; font-size: 34px;
    color: var(--emboss); margin-top: 12px; line-height: 1;
  }
  .back-brand__tagline {
    font-family: "Open Sans", sans-serif;
    font-weight: 600; font-size: 12px; letter-spacing: 1.6px;
    color: var(--emboss); margin-top: 8px;
  }
</style>
</head>
<body>

<section class="card card--front" aria-label="Business card front">
  <svg class="wave" viewBox="0 0 540 309" preserveAspectRatio="none" aria-hidden="true">
    <path d="M540 70 C 420 80, 350 100, 330 160 C 315 220, 245 285, 140 309" fill="none" stroke="var(--seafoam)" stroke-width="7"/>
    <path d="M540 85 C 430 95, 365 115, 345 165 C 330 225, 260 290, 160 309 L540 309 Z" fill="var(--ocean)"/>
    <path d="M0 294 C 70 300, 150 301, 230 296 L230 309 L0 309 Z" fill="var(--seafoam)"/>
    <path d="M40 303 C 110 305, 170 304, 230 300 L230 309 L40 309 Z" fill="var(--ocean-deep)"/>
  </svg>

  <div class="name-tab"></div>
  <div class="person">
    <div class="person__name">Marcus Ellery</div>
    <div class="person__role">Manager</div>
  </div>

  <div class="brand">
    <div class="brand__dot"></div>
    <div>
      <div class="brand__name">Bayhaven Grins</div>
      <div class="brand__tagline">Pediatric Dentistry &amp; Orthodontics</div>
    </div>
  </div>

  <p class="address">123 Street, city<br>state, ZIP 0000</p>

  <ul class="contact">
    <li>123-456-7800
      <svg viewBox="0 0 12 12" aria-hidden="true"><circle cx="6" cy="6" r="6" fill="var(--white)"/><path d="M3.6 3.2 L5 3 L5.6 4.6 L4.8 5.2 C5.2 6.1 5.9 6.8 6.8 7.2 L7.4 6.4 L9 7 L8.8 8.4 C6 8.6 3.4 6 3.6 3.2Z" fill="var(--ocean)"/></svg>
    </li>
    <li>office@bayhavengrins.com
      <svg viewBox="0 0 12 12" aria-hidden="true"><rect x="0.5" y="2" width="11" height="8" fill="var(--white)"/><path d="M0.5 2 L6 6.5 L11.5 2" fill="none" stroke="var(--ocean)" stroke-width="1"/></svg>
    </li>
    <li>www.bayhavengrins.com
      <svg viewBox="0 0 12 12" aria-hidden="true"><circle cx="6" cy="6" r="5.5" fill="var(--white)"/><ellipse cx="6" cy="6" rx="2.3" ry="5.5" fill="none" stroke="var(--ocean)" stroke-width="0.9"/><path d="M0.5 6 H11.5" stroke="var(--ocean)" stroke-width="0.9"/></svg>
    </li>
  </ul>
</section>

<section class="card card--back" aria-label="Business card back">
  <div class="back-brand">
    <div class="back-brand__dot"></div>
    <div class="back-brand__name">Bayhaven Grins</div>
    <div class="back-brand__tagline">Pediatric Dentistry &amp; Orthodontics</div>
  </div>
</section>

</body>
</html>
```